Car Detailing product label for 750ML Clear Bottle

I need a label for various product with differente color for each products but in the same size bottle each time. It's only for our purpose no commercial application. I need a template with differente color but same design. The name for product it's : Tidal Quartz. We dont have any logo because it's only for us. We like like car silhouette in the logo or in background or something like that.

And for the product we have many like : APC Cleaner, Drying Aid, Wheel Cleaner and some other.

```html
<!DOCTYPE html>
<html lang="en">
<head>
<meta charset="utf-8">
<title>Tidal Quartz – Detailing Labels</title>
<link rel="stylesheet" href="https://fonts.googleapis.com/css2?family=Anton&family=Oswald:wght@500;700&display=swap">
<style>
  :root {
    --page: #ffffff;
    --ink: #0a0a0a;
    --white: #ffffff;
    --red: #e31e24;
    --orange: #f26522;
    --road-dark: #1b1d20;
    --road-mid: #3a3d42;
  }
  * { margin: 0; padding: 0; box-sizing: border-box; }
  html, body { width: 1200px; height: 1200px; overflow: hidden; background: var(--page); }
  .canvas { position: relative; width: 1200px; height: 1200px; }

  .label {
    position: absolute;
    width: 636px;
    height: 478px;
    background: var(--ink);
    overflow: hidden;
    font-family: "Anton", "Oswald", sans-serif;
    color: var(--white);
  }
  .label--all-purpose { left: 44px; top: 52px; --accent: var(--red); }
  .label--leather { left: 515px; top: 648px; --accent: var(--orange); }

  .label__band {
    position: absolute; inset: 0;
    z-index: 0;
    background: var(--accent);
    clip-path: polygon(0 0, 208px 0, 208px 192px, 174px 192px, 174px 100%, 0 100%);
  }
  .label__photo {
    position: absolute;
    z-index: 1;
    left: 174px; top: 192px;
    width: 462px; height: 170px;
    background:
      linear-gradient(180deg, rgba(10,10,10,0.6) 0%, rgba(10,10,10,0) 20%, rgba(10,10,10,0) 65%, var(--ink) 100%),
      radial-gradient(ellipse 40% 60% at 50% 45%, #4a4d53 0%, var(--road-mid) 45%, var(--road-dark) 100%);
  }
  .label__brand-vertical,
  .label__variant-vertical,
  .label__brand,
  .label__title,
  .label__variant,
  .label__volume { z-index: 2; }

  .label__brand-vertical {
    position: absolute;
    left: 86px; top: 240px;
    transform: translate(-50%, -50%) rotate(-90deg);
    text-align: center;
    font-size: 70px;
    line-height: 0.95;
    letter-spacing: 1px;
    white-space: nowrap;
    color: var(--white);
  }
  .label__variant-vertical {
    position: absolute;
    left: 192px; top: 112px;
    transform: translate(-50%, -50%) rotate(-90deg);
    font-family: "Oswald", sans-serif;
    font-weight: 500;
    font-size: 17px;
    line-height: 1;
    white-space: nowrap;
    letter-spacing: 0.3px;
  }
  .label__brand {
    position: absolute;
    left: 396px; top: 60px;
    transform: translateX(-50%);
    font-size: 44px;
    white-space: nowrap;
    letter-spacing: 1px;
    color: var(--white);
  }
  .label__title {
    position: absolute;
    left: 396px; top: 292px;
    transform: translateX(-50%);
    font-size: 88px;
    line-height: 1;
    white-space: nowrap;
    -webkit-text-stroke: 3px var(--accent);
    paint-order: stroke fill;
  }
  .label__variant {
    position: absolute;
    left: 246px; top: 380px;
    width: 302px; height: 50px;
    background: var(--accent);
    border-radius: 8px;
    display: flex; align-items: center; justify-content: center;
    font-family: "Oswald", sans-serif;
    font-weight: 700;
    font-size: 40px;
    white-space: nowrap;
  }
  .label--leather .label__variant { font-size: 38px; }
  .label__volume {
    position: absolute;
    left: 396px; top: 440px;
    transform: translateX(-50%);
    font-family: "Oswald", sans-serif;
    font-weight: 700;
    font-size: 16px;
  }
</style>
</head>
<body>
<main class="canvas">

  <section class="label label--all-purpose">
    <div class="label__band"></div>
    <div class="label__photo" role="img" aria-label="Photo of a dark grey sports saloon driving toward the viewer on a night road with yellow lane lines"></div>
    <div class="label__brand-vertical">TIDAL<br>QUARTZ</div>
    <div class="label__variant-vertical">ALL PURPOSE</div>
    <div class="label__brand">TIDAL QUARTZ</div>
    <div class="label__title">CLEANER</div>
    <div class="label__variant">ALL PURPOSE</div>
    <div class="label__volume">750ML</div>
  </section>

  <section class="label label--leather">
    <div class="label__band"></div>
    <div class="label__photo" role="img" aria-label="Photo of a dark grey sports saloon driving toward the viewer on a night road with yellow lane lines"></div>
    <div class="label__brand-vertical">TIDAL<br>QUARTZ</div>
    <div class="label__variant-vertical">LEATHER &amp; VINYL</div>
    <div class="label__brand">TIDAL QUARTZ</div>
    <div class="label__title">CLEANER</div>
    <div class="label__variant">LEATHER &amp; VINYL</div>
    <div class="label__volume">750ML</div>
  </section>

</main>
</body>
</html>
```